Veloran Dental Development - Business Cards

We are a Dental Development and Management company. We are looking to develop a new business card design. We are business professional but modern. The logo that I have attached is the business colors. You can also check out our website for further detail. www.veloranmgmt-example.com

Target Market(s)

Dental Professionals, Dentists and Office Staff, Marketing Professionals

Industry/Entity Type

Business

Requirements
Must have
• Name - Bartholomew K. Tressing
Title - Marketing Director
Phone - 555-019-4827
Cell - 555-019-4827
Email - Bart.t@veloran-example.com
Address - 2917 W Larkmoor Rd, Mesa, AZ 85209
Web- www.veloran-example.com

Veloran Logo must go on the front. The other logos go on the back as affiliated businesses

Must be editable to enter specific Names, Positions, Phone numbers and email later on. Using Adobe CS5 currently.

```html
<!DOCTYPE html>
<html lang="en">
<head>
<meta charset="utf-8">
<title>Veloran Dental Development – Business Cards</title>
<link href="https://fonts.googleapis.com/css2?family=Libre+Baskerville:wght@400;700&family=Arimo:wght@700&display=swap" rel="stylesheet">
<style>
  :root {
    --navy: #232a5e;
    --navy-deep: #1c2250;
    --gold: #e09a2c;
    --white: #ffffff;
    --backdrop-top: #ffffff;
    --backdrop-bottom: #e4e4e4;
    --red: #e3262c;
    --teal: #1f6f8b;
    --plan-red: #b8282e;
    --royal: #2b3a93;
    --purple: #5b2a86;
  }
  * { margin: 0; padding: 0; box-sizing: border-box; }
  html, body { width: 1200px; height: 1000px; overflow: hidden; }
  body {
    background: linear-gradient(to bottom, var(--backdrop-top) 0%, var(--backdrop-bottom) 100%);
    position: relative;
    font-family: "Libre Baskerville", serif;
  }
  .card {
    position: absolute;
    top: 244px;
    width: 320px;
    height: 512px;
    background: var(--white);
    box-shadow: 0 2px 6px rgba(0,0,0,0.12);
    overflow: hidden;
  }
  .card--front { left: 250px; }
  .card--back { left: 630px; }

  /* Front */
  .front__header {
    height: 182px;
    display: flex;
    align-items: center;
    padding-left: 34px;
  }
  .brand-name {
    color: var(--navy);
    font-weight: 700;
    font-size: 19px;
    line-height: 1.3;
  }
  .front__rule { height: 10px; background: var(--gold); }
  .front__body {
    position: absolute;
    top: 192px; left: 0; right: 0; bottom: 0;
    background: linear-gradient(to bottom, var(--navy) 0%, var(--navy-deep) 100%);
    padding: 50px 0 0 30px;
  }
  .person-name {
    color: var(--white);
    font-weight: 700;
    font-size: 18px;
  }
  .person-title {
    color: var(--gold);
    font-size: 14px;
    margin-top: 6px;
  }
  .contact-list {
    position: absolute;
    left: 18px;
    top: 212px;
    list-style: none;
    font-family: "Arimo", sans-serif;
    font-weight: 700;
    font-size: 12px;
    line-height: 17px;
    color: var(--gold);
  }
  .contact-list .label { color: var(--white); margin-right: 4px; }

  /* Back */
  .affiliate-list {
    list-style: none;
    padding: 40px 0 0 0;
    display: flex;
    flex-direction: column;
    gap: 44px;
  }
  .affiliate {
    display: flex;
    align-items: center;
    gap: 8px;
    font-weight: 700;
    font-size: 17px;
    line-height: 1.2;
  }
  .affiliate--centers { padding-left: 34px; color: var(--teal); }
  .affiliate--plan { padding-left: 110px; color: var(--plan-red); }
  .affiliate--emergency { padding-left: 30px; color: var(--royal); }
  .affiliate--pediatric { padding-left: 110px; color: var(--purple); font-size: 15px; }
  .affiliate__mark {
    width: 40px; height: 40px;
    background: var(--red);
    flex: none;
  }
  .affiliate__badge {
    width: 40px; height: 40px;
    border-radius: 50%;
    background: #3ab4e6;
    flex: none;
  }
</style>
</head>
<body>
  <section class="card card--front" aria-label="Business card front">
    <header class="front__header">
      <div class="brand-name">Veloran<br>Dental Development</div>
    </header>
    <div class="front__rule"></div>
    <div class="front__body">
      <p class="person-name">Bartholomew K. Tressing</p>
      <p class="person-title">Marketing Director</p>
      <ul class="contact-list">
        <li><span class="label">p.</span>555-019-4827</li>
        <li><span class="label">c.</span>555-019-4827</li>
        <li><span class="label">e.</span>Bart.t@veloran-example.com</li>
        <li><span class="label">a.</span>2917 W Larkmoor Rd, Mesa, AZ 85209</li>
        <li><span class="label">w.</span>www.veloran-example.com</li>
      </ul>
    </div>
  </section>

  <section class="card card--back" aria-label="Business card back with affiliated businesses">
    <ul class="affiliate-list">
      <li class="affiliate affiliate--centers">Hearthside<br>Dental Centers</li>
      <li class="affiliate affiliate--plan">Hearthside<br>Dental Plan</li>
      <li class="affiliate affiliate--emergency"><span class="affiliate__mark"></span>Rapidcare<br>Dental Centers</li>
      <li class="affiliate affiliate--pediatric"><span class="affiliate__badge"></span>Brightsprout<br>Pediatric Dental</li>
    </ul>
  </section>
</body>
</html>
```